real estate agent looking for a business card

I am trying to brand myself and my team in the local real estate business. We just received new logo and we want to combine that with brandon Ashcroft logo.

I want my business card to look elegant, super sharp, and professional, but also, personable, because the brand is me myself.

About me; I sell only residential real estate, that is including single family homes, condominiums, vacant lands.

Reason: I am trying to get opinions of my team members about final logo selection.

Reason: During the holiday season, some of the members on vacation.

Target Market(s)

to consumers ages between 25-75

Industry/Entity Type

Real Estate Agent

Contact Information for Business Card

Name: Selin Odak-Branwell "Realtor"
Cell: (248) 555-0143
Direct Line: (248) 555-0187
Fax: (248) 555-0162
selinodak@maplenetmail.net
selin.bahomes.example

address: 41200 Pinecrest Parkway Suite:200
Farmington Hills, Mi 48990
Smaller font: Each office independently Owned and operated.
I want Brandon Ashcroft logo to be small and The Selin Group Logo to be visible.
My picture shall be on the right side
I prefer the background color to be black.

Font styles to use
Other font styles liked:
• i am flexible with font. i dont want script or decorative fonts though.

Requirements
Must have
• our tag line : Keys to Your Next Chapter
Nice to have
• we want to look very sharp and elegant. something uniq looking business card.

```html
<!DOCTYPE html>
<html lang="en">
<head>
<meta charset="utf-8">
<title>The Selin Group — Business Card</title>
<link rel="stylesheet" href="https://fonts.googleapis.com/css2?family=Questrial&display=swap">
<style>
  :root {
    --backdrop: #2a2623;
    --card: #141414;
    --card-deep: #0b0b0b;
    --stripe: rgba(255,255,255,0.035);
    --gold: #d9a62a;
    --red: #c8242f;
    --white: #f2f2f2;
    --muted: #cfcfcf;
  }
  * { box-sizing: border-box; margin: 0; padding: 0; }
  html, body { width: 1200px; height: 1200px; overflow: hidden; }
  body {
    background: var(--backdrop);
    font-family: "Questrial", "Century Gothic", sans-serif;
    position: relative;
  }
  .card {
    position: absolute;
    top: 215px;
    width: 440px;
    height: 770px;
    background: linear-gradient(160deg, var(--card) 0%, var(--card-deep) 100%);
    overflow: hidden;
    box-shadow: 0 12px 30px rgba(0,0,0,0.45);
  }
  .card--front { left: 120px; }
  .card--back { left: 640px; }

  .stripes {
    position: absolute; inset: 0;
    background: repeating-linear-gradient(90deg, transparent 0 54px, var(--stripe) 54px 56px);
  }

  /* front */
  .portrait {
    position: absolute;
    right: 0; top: 60px;
    width: 270px; height: 710px;
    background: linear-gradient(180deg, #c9a675 0%, #d8c3aa 18%, #1d1d1f 40%, #101012 100%);
    border-radius: 120px 0 0 0;
  }
  .front-brand {
    position: absolute;
    left: 36px; top: 470px;
    right: 24px;
  }
  .brand-name {
    color: var(--gold);
    font-size: 44px;
    line-height: 1;
    letter-spacing: 1px;
    white-space: nowrap;
  }
  .brand-name--small { font-size: 40px; }
  .tagline {
    color: var(--red);
    font-size: 15px;
    margin-top: 8px;
    letter-spacing: 0.5px;
  }
  .agent-name {
    color: var(--white);
    font-size: 28px;
    margin-top: 26px;
  }
  .agent-title {
    color: var(--gold);
    font-size: 24px;
    letter-spacing: 3px;
    margin-top: 6px;
  }
  .brokerage {
    position: absolute;
    left: 36px; bottom: 34px;
    color: var(--white);
    font-size: 17px;
    letter-spacing: 1.5px;
    text-transform: uppercase;
  }

  /* back */
  .back-brand {
    position: absolute;
    left: 60px; top: 70px;
  }
  .back-details {
    position: absolute;
    left: 40px; top: 280px;
    right: 30px;
  }
  .contact-list {
    list-style: none;
    margin-top: 22px;
  }
  .contact-list li {
    display: flex;
    align-items: center;
    gap: 14px;
    color: var(--white);
    font-size: 20px;
    margin-bottom: 12px;
  }
  .contact-list svg { width: 18px; height: 18px; flex: none; fill: var(--gold); }
  .contact-list .email { font-size: 17px; }
  .website {
    color: var(--red);
    font-size: 20px;
    margin-top: 4px;
  }
  .faded-portrait {
    position: absolute;
    right: -20px; bottom: -30px;
    width: 300px; height: 330px;
    border-radius: 50%;
    background: radial-gradient(circle at 50% 45%, rgba(150,140,130,0.45) 0%, rgba(60,56,52,0.3) 50%, transparent 72%);
  }
</style>
</head>
<body>

<section class="card card--front">
  <div class="stripes"></div>
  <div class="portrait" role="img" aria-label="Portrait photo of the agent in a dark blazer and white blouse"></div>
  <div class="front-brand">
    <div class="brand-name">The Selin Group</div>
    <div class="tagline">Keys to Your Next Chapter</div>
    <div class="agent-name">Selin Odak-Branwell</div>
    <div class="agent-title">REALTOR</div>
  </div>
  <div class="brokerage">Brandon Ashcroft</div>
</section>

<section class="card card--back">
  <div class="faded-portrait" role="img" aria-label="Faint toned portrait photo of the agent"></div>
  <div class="back-brand">
    <div class="brand-name brand-name--small">The Selin Group</div>
    <div class="tagline">Keys to Your Next Chapter</div>
  </div>
  <div class="back-details">
    <div class="agent-name">Selin Odak-Branwell</div>
    <div class="agent-title">REALTOR</div>
    <ul class="contact-list">
      <li>
        <svg viewBox="0 0 18 18" aria-hidden="true"><path d="M5 1h8a1 1 0 0 1 1 1v14a1 1 0 0 1-1 1H5a1 1 0 0 1-1-1V2a1 1 0 0 1 1-1zm1 2v10h6V3zm3 11.2a.9.9 0 1 0 0 1.8.9.9 0 0 0 0-1.8z"/></svg>
        (248) 555-0143
      </li>
      <li>
        <svg viewBox="0 0 18 18" aria-hidden="true"><path d="M2 6c0-2 3-3 7-3s7 1 7 3v1h-4V5.5H6V7H2zm3 2h8l2 8H3zm4 2a2 2 0 1 0 0 4 2 2 0 0 0 0-4z"/></svg>
        (248) 555-0187
      </li>
      <li>
        <svg viewBox="0 0 18 18" aria-hidden="true"><path d="M5 1h7l2 2v4H5zM2 8h14a1 1 0 0 1 1 1v7a1 1 0 0 1-1 1H2a1 1 0 0 1-1-1V9a1 1 0 0 1 1-1zm2 2v2h3v-2zm6 0v1h4v-1zm0 2v1h4v-1z"/></svg>
        (248) 555-0162
      </li>
      <li class="email">
        <svg viewBox="0 0 18 18" aria-hidden="true"><path d="M1 4h16v10H1zm1.5 1.2L9 10l6.5-4.8z"/></svg>
        selinodak@maplenetmail.net
      </li>
    </ul>
    <div class="website">selin.bahomes.example</div>
  </div>
  <div class="brokerage">Brandon Ashcroft</div>
</section>

</body>
</html>
```